Verano Suisse: Symposium annuel 2018

You created the flyer "Atelier Dorvanne" for us at the beginning of the year. We would like to work in a new version. More details can be found in the briefing! Flyer (red, gray, black) - flyer wants to be white! - Flyer wants to be White! All further information can be found in the document in the appendix!

```html
<!DOCTYPE html>
<html lang="fr">
<head>
<meta charset="utf-8">
<title>Verano Suisse – Symposium annuel 2018</title>
<link href="https://fonts.googleapis.com/css2?family=Oswald:wght@300;400;500&family=Roboto:ital,wght@0,400;0,500;1,500;1,700&display=swap" rel="stylesheet">
<style>
  :root {
    --red: #e41e26;
    --ink: #111111;
    --paper: #ffffff;
    --backdrop: #ececec;
    --sponsor: #1f3f8f;
  }
  * { margin: 0; padding: 0; box-sizing: border-box; }
  html, body { width: 1200px; height: 900px; overflow: hidden; background: var(--backdrop); }
  .flyer {
    position: absolute; left: 27px; top: 45px; width: 1146px; height: 810px;
    background: var(--paper); color: var(--ink);
    font-family: 'Roboto', sans-serif; overflow: hidden;
  }
  .flyer > * { position: absolute; z-index: 1; }
  .flyer > .texture, .flyer > .texture-right, .flyer > .anatomy { z-index: 0; }
  .texture {
    left: 0; top: 0; width: 620px; height: 420px;
    background: radial-gradient(ellipse at 30% 35%, #f1f1f1 0%, rgba(255,255,255,0) 65%);
  }
  .texture-right {
    left: 560px; top: 360px; width: 586px; height: 450px;
    background: radial-gradient(ellipse at 60% 60%, #f3f3f3 0%, rgba(255,255,255,0) 65%);
  }
  .anatomy {
    left: 400px; top: 262px; width: 160px; height: 300px;
    background: linear-gradient(180deg, rgba(225,225,225,0.5) 0%, #dedede 50%, rgba(240,240,240,0.6) 100%);
    border-radius: 70px 70px 12px 12px;
  }
  .title {
    left: 60px; top: 80px; width: 494px; text-align: center;
    font-family: 'Oswald', sans-serif; font-weight: 300; color: var(--red);
    font-size: 56px; line-height: 65px; letter-spacing: -0.5px;
  }
  .date {
    left: 152px; top: 240px; width: 300px; text-align: center;
    font-family: 'Oswald', sans-serif; font-weight: 400; font-size: 26px; line-height: 30px;
    letter-spacing: -0.5px;
  }
  .credits { left: 38px; top: 362px; }
  .credits h2 {
    font-family: 'Oswald', sans-serif; font-weight: 400; color: var(--red);
    font-size: 19px; margin-bottom: 10px;
  }
  .credits p { color: var(--red); font-size: 14px; line-height: 24px; }
  .inscription { left: 38px; top: 566px; width: 534px; }
  .inscription h2 {
    font-family: 'Oswald', sans-serif; font-weight: 400; font-size: 25px; margin-bottom: 12px;
  }
  .inscription p { font-size: 15px; line-height: 31px; white-space: nowrap; overflow: hidden; }
  .brand {
    left: 38px; top: 730px; display: flex; align-items: center; gap: 6px;
    font-family: 'Oswald', sans-serif; font-weight: 500; font-size: 19px; line-height: 20px;
    text-transform: uppercase; width: 120px;
  }
  .brand .mark { width: 14px; height: 14px; background: var(--ink); flex: none; }
  .return {
    left: 196px; top: 726px;
    font-family: 'Oswald', sans-serif; font-weight: 400; font-size: 15px; line-height: 26px;
    letter-spacing: -0.3px;
  }
  .return .contact { color: var(--red); font-family: 'Roboto', sans-serif; font-size: 14px; }
  .section-head {
    left: 611px; width: 509px;
    font-family: 'Oswald', sans-serif; font-weight: 400; color: var(--red);
    font-size: 19px; letter-spacing: -0.3px; padding-bottom: 8px;
    border-bottom: 3px solid var(--ink);
  }
  .programme-head { top: 44px; }
  .sponsors-head { top: 599px; }
  .session { left: 611px; width: 480px; display: flex; font-size: 14px; line-height: 17.5px; }
  .session .time { color: var(--red); font-weight: 500; width: 102px; flex: none; }
  .session .talk { font-style: italic; font-weight: 700; }
  .session .speaker { font-style: normal; font-weight: 400; display: block; }
  .sponsor {
    font-family: 'Roboto', sans-serif; font-weight: 500; color: var(--sponsor);
    font-size: 17px; display: flex; align-items: center; justify-content: center; gap: 6px;
    white-space: nowrap;
  }
  .sponsor .mark { width: 11px; height: 11px; background: var(--sponsor); flex: none; }
</style>
</head>
<body>
<main class="flyer">
  <div class="texture" role="img" aria-label="Motif réseau gris clair en arrière-plan"></div>
  <div class="texture-right" role="img" aria-label="Motif réseau gris clair en arrière-plan"></div>
  <div class="anatomy" role="img" aria-label="Illustration du système lymphatique du buste humain"></div>

  <h1 class="title">SYMPOSIUM ANNUEL<br>VERANO SUISSE</h1>
  <p class="date">27 SEPTEMBRE 2018<br>DE 14H00 À 18H00</p>

  <section class="credits">
    <h2>CRÉDITS : 4</h2>
    <p>SOCIÉTÉ ALPINE D’ANGIOLOGIE</p>
    <p>&nbsp;MÉDECINE INTERNE GÉNÉRALE</p>
  </section>

  <section class="inscription">
    <h2>INSCRIPTION</h2>
    <p>NOM........................................................PRÉNOM...............................................................</p>
    <p>TIMBRE ET SIGNATURE:.............................................................................................................</p>
  </section>

  <div class="brand"><span class="mark"></span><span>Verano<br>Suisse</span></div>
  <p class="return">BULLETIN D’INSCRIPTION À RETOURNER :<br>PAR FAX <span class="contact">021 480 52 90</span> ou E-MAIL : <span class="contact">contact@veranosuisse.ch</span></p>

  <h2 class="section-head programme-head">ACTUALISATION DES CONNAISSANCES EN LYMPHOLOGIE</h2>

  <div class="session" style="top:110px"><span class="time">14:00 -14:10</span><span class="talk">Bienvenue</span></div>
  <div class="session" style="top:145px"><span class="time">14:10 -14:40</span><span class="talk">A la découverte des lymphatiques : place de l’IRM<span class="speaker">Pr L. Ferrante, University of Castelmonte, Italy</span></span></div>
  <div class="session" style="top:198px"><span class="time">14:45 -15:15</span><span class="talk">Une entité nouvelle : le système « glymphatique »<span class="speaker">M. R. Lindqvist, Service d’Angiologie, CHRV, Lausanne</span></span></div>
  <div class="session" style="top:251px"><span class="time">15:20 - 15:50</span><span class="talk">Approche psychosomatique du lymphœdème<span class="speaker">Dr K. Albrecht, biologiste et psychologue, cabinet spécialisé en psycho-oncologie, Heidelberg, Allemagne</span></span></div>
  <div class="session" style="top:321px"><span class="time">15:50 - 16:10</span><span class="talk">Pause</span></div>
  <div class="session" style="top:357px"><span class="time">16:10 - 16:40</span><span class="talk">Prévenir le lymphœdème lors de la chirurgie oncologique: l’expérience LYVENA<span class="speaker">Pr G. Valdieri, Université de Portavela, Italie</span></span></div>
  <div class="session" style="top:427px"><span class="time">16:45 - 17:15</span><span class="talk">Quand traiter le lymphœdème par voie chirurgicale ?<span class="speaker">Dr A. Bernasconi, Service de chirurgie plastique et reconstructive, CHRV, Lausanne</span></span></div>
  <div class="session" style="top:497px"><span class="time">17:20 - 17:50</span><span class="talk">Le vaisseau lymphatique artificiel : mythe ou réalité ?<span class="speaker">Pr C. Morandi, Service d’Angiologie, CHRV, Lausanne</span></span></div>
  <div class="session" style="top:550px"><span class="time">17 :55 - 18.00</span><span class="talk">Conclusion</span></div>

  <h2 class="section-head sponsors-head">NOUS REMERCIONS CHALEUREUSEMENT NOS SPONSORS</h2>

  <div class="sponsor" style="left:611px;top:662px;width:140px"><span class="mark"></span>Norvex Medical</div>
  <div class="sponsor" style="left:766px;top:662px;width:148px">Talmo</div>
  <div class="sponsor" style="left:938px;top:662px;width:166px">medivia</div>
  <div class="sponsor" style="left:695px;top:730px;width:142px;font-size:15px">Hartwig &amp; Selm</div>
  <div class="sponsor" style="left:872px;top:730px;width:100px;font-size:15px"><span class="mark"></span>Elvaris</div>
</main>
</body>
</html>
```